Marwell Herd Services concrete grooving services flyer design

Marwell Herd Services offers 4 different grooving options:

DEEP GROOVING
, ideal for Safety & Efficiency
Our hugely popular deep straight line grooving, long lasting, minimal hoof wear,

Create safe and secure flooring, cows walk without hesitation

Achieve groove spacing for optimal hoof function, reduce hoof trauma

Ideal grooves to new concrete or surfaces with little to no pattern or previous grooving

Ideal groove pattern as promoted by The pasturewide programme

MINI GROOVING,
Smaller dimensions Ideal option for heifer housing and high activity areas such as parlours and handling areas

An ideal solution for regaining traction on old previous grooving that has lost its traction without loosing stability

Plaining

smoothing down rough concrete with previous aggressive grooving or patterns to reduce hoof trauma & wear

SENSOR PLATE SINKING

sinking sensor plates for automated machines below surface level preventing accidental damage & wear

```html
<!DOCTYPE html>
<html lang="en">
<head>
<meta charset="utf-8">
<title>Marwell Herd Services – Concrete Grooving</title>
<link href="https://fonts.googleapis.com/css2?family=Source+Sans+3:wght@400;600;700;800&display=swap" rel="stylesheet">
<style>
:root{
  --green:#8cc63f;
  --dark-green:#17713a;
  --ink:#111;
  --text:#1d1d1d;
  --muted:#555;
  --paper:#eef0ef;
  --white:#fff;
}
*{margin:0;padding:0;box-sizing:border-box}
html,body{width:837px;height:1200px;overflow:hidden}
body{font-family:"Source Sans 3",sans-serif;color:var(--text);background:var(--paper)}
.flyer{position:relative;width:837px;height:1200px;overflow:hidden;
  background:linear-gradient(180deg,#e4e7e6 0%,#eef0ef 40%,#f3f2ee 70%,#f6f6f4 100%)}
.backdrop{position:absolute;inset:0;
  background:linear-gradient(160deg,rgba(200,205,203,.5) 0%,rgba(235,237,236,.2) 45%,rgba(225,215,195,.35) 75%,rgba(245,245,243,.3) 100%)}
.deco{position:absolute;left:0;top:0}
.brand{position:absolute;left:105px;top:60px;display:flex;align-items:center;gap:10px}
.brand-dot{width:22px;height:22px;border-radius:50%;background:var(--dark-green)}
.brand-name{font-weight:700;font-size:25px;color:var(--ink);line-height:1.1;width:170px}
.tagline{position:absolute;left:89px;top:216px;font-size:18.5px;letter-spacing:4.6px;line-height:23px;color:var(--ink);font-weight:400}
.section-title{position:absolute;left:31px;top:298px;font-size:37px;font-weight:800;letter-spacing:7.5px;color:var(--ink)}
.section-title span{color:var(--dark-green)}
.service-photo{position:absolute;left:18px;width:168px;height:168px;border:6px solid var(--green);border-radius:22px}
.service{position:absolute;left:196px;width:610px}
.service h2{font-size:19px;font-weight:600;color:var(--ink);letter-spacing:-.2px;line-height:24px}
.service h2::after{content:"";display:block;margin-left:34px;width:108px;height:2px;background:var(--green)}
.service .sub{margin:8px 0 0 20px;font-size:14.5px;letter-spacing:1.6px;color:var(--ink)}
.service ul{list-style:none;margin:10px 0 0 20px}
.service li{position:relative;padding-left:15px;font-size:14.6px;line-height:19px;color:var(--text)}
.service li::before{content:"";position:absolute;left:0;top:5px;border-left:8px solid var(--green);border-top:5px solid transparent;border-bottom:5px solid transparent}
.service li.cont::before{display:none}
.footer{position:absolute;left:18px;top:1129px;width:801px;height:57px}
.footer svg{position:absolute;inset:0}
.contact{position:absolute;top:0;height:57px;display:flex;align-items:center;color:var(--white);font-size:23px;letter-spacing:.3px}
.contact svg{position:static;margin-right:14px}
</style>
</head>
<body>
<div class="flyer">
  <div class="backdrop"></div>

  <svg class="deco" width="837" height="1200" viewBox="0 0 837 1200">
    <defs>
      <linearGradient id="barnTones" x1="0" y1="0" x2="0.6" y2="1">
        <stop offset="0" stop-color="#9aa5a0"/>
        <stop offset="0.45" stop-color="#5c6466"/>
        <stop offset="1" stop-color="#b48a52"/>
      </linearGradient>
    </defs>
    <!-- tagline band -->
    <path d="M0 210 H470 L540 270 H0 Z" fill="var(--green)"/>
    <path d="M31 222 H64 Q79 222 79 239 Q79 256 64 256 H31 Z" fill="var(--dark-green)"/>
    <!-- hero image -->
    <path role="img" aria-label="Photo of the grooving machine working on a wet concrete floor inside a cattle barn"
      d="M414 0 H837 V410 Q830 462 770 437 L450 190 Q352 115 414 0 Z"
      fill="url(#barnTones)" stroke="var(--green)" stroke-width="6" stroke-linejoin="round"/>
    <!-- right-side diagonal accents -->
    <line x1="860" y1="560" x2="695" y2="725" stroke="var(--green)" stroke-width="110" stroke-linecap="round"/>
    <line x1="860" y1="670" x2="820" y2="710" stroke="var(--dark-green)" stroke-width="52" stroke-linecap="round"/>
    <line x1="880" y1="820" x2="772" y2="905" stroke="var(--green)" stroke-width="92" stroke-linecap="round"/>
    <line x1="870" y1="955" x2="830" y2="976" stroke="var(--dark-green)" stroke-width="52" stroke-linecap="round"/>
  </svg>

  <div class="brand">
    <div class="brand-dot"></div>
    <div class="brand-name">Marwell Herd Services</div>
  </div>

  <p class="tagline">THE BEST CONCRETE GROOVING<br>SERVICES</p>

  <h1 class="section-title">SERVICES <span>OFFERED</span></h1>

  <div class="service-photo" style="top:362px;background:linear-gradient(180deg,#8d9596 0%,#b98a3f 55%,#9a6c28 100%)" role="img" aria-label="Photo of deep straight-line grooves in a wet barn floor"></div>
  <div class="service-photo" style="top:550px;background:linear-gradient(160deg,#8b8680 0%,#6a6762 50%,#4c4a47 100%)" role="img" aria-label="Photo of fine mini grooving on a concrete walkway"></div>
  <div class="service-photo" style="top:737px;background:linear-gradient(180deg,#9aa0a2 0%,#8f8a82 40%,#4f5356 100%)" role="img" aria-label="Photo of a smoothed planed strip along a concrete floor"></div>
  <div class="service-photo" style="top:925px;background:linear-gradient(180deg,#5e6466 0%,#8c8577 50%,#6f8fa8 100%)" role="img" aria-label="Photo of a floor saw cutting a recess for a sensor plate in a cattle shed"></div>

  <section class="service" style="top:366px">
    <h2>1. DEEP GROOVING</h2>
    <p class="sub">ideal for Safety &amp; Efficiency</p>
    <ul>
      <li>Our hugely popular deep straight line grooving, long lasting,</li>
      <li class="cont">minimal hoof wear.</li>
      <li>Create safe and secure flooring, cows walk without hesitation</li>
      <li class="cont">Achieve groove spacing for optimal hoof function, reduce hoof trauma</li>
      <li>Ideal grooves to new concrete or surfaces with little to no pattern or previous grooving</li>
      <li class="cont">Ideal groove pattern as promoted by The pasturewide programme</li>
    </ul>
  </section>

  <section class="service" style="top:568px">
    <h2>2. MINI GROOVING</h2>
    <ul style="margin-top:12px">
      <li>Smaller dimensions Ideal option for heifer housing and high activity areas</li>
      <li class="cont">such as parlours and handling areas</li>
      <li>An ideal solution for regaining traction on old previous grooving</li>
      <li class="cont">that has lost its traction without loosing stability</li>
    </ul>
  </section>

  <section class="service" style="top:774px">
    <h2>3. PLAINING</h2>
    <ul style="margin-top:12px">
      <li>Smoothing down rough concrete with previous aggressive grooving or patterns</li>
      <li class="cont">to reduce hoof trauma &amp; wear</li>
    </ul>
  </section>

  <section class="service" style="top:945px">
    <h2>4. SENSOR PLATE SINKING</h2>
    <ul style="margin-top:12px">
      <li>Our hugely popular deep straight line grooving, long lasting, minimal hoof wear,</li>
      <li>Create safe and secure flooring, cows walk without hesitation</li>
      <li>Achieve groove spacing for optimal hoof function, reduce hoof trauma</li>
      <li>Ideal grooves to new concrete or surfaces with little to no pattern or previous grooving</li>
      <li>Ideal groove pattern as promoted by The pasturewide programme</li>
    </ul>
  </section>

  <footer class="footer">
    <svg width="801" height="57" viewBox="0 0 801 57"><path d="M0 0 H771 L801 57 H0 Z" fill="var(--green)"/></svg>
    <div class="contact" style="left:23px">
      <svg width="22" height="22" viewBox="0 0 24 24" fill="none" stroke="#333" stroke-width="1.6"><circle cx="12" cy="12" r="11"/><path d="M8 6.5l2 2.5-1.2 1.6c.8 1.7 2 2.9 3.6 3.6l1.6-1.2 2.5 2-1.3 1.7c-3.9-.4-7.7-4.2-8.1-8.1z"/></svg>
      CALL NOW : +000 1234 5678
    </div>
    <div class="contact" style="left:367px">
      <svg width="26" height="26" viewBox="0 0 24 24" fill="none" stroke="#333" stroke-width="1.5"><circle cx="12" cy="12" r="10.5"/><ellipse cx="12" cy="12" rx="4.5" ry="10.5"/><path d="M1.5 12h21M3 7h18M3 17h18"/></svg>
      <span style="margin-left:4px">www.marwellherdservices.com</span>
    </div>
  </footer>
</div>
</body>
</html>
```